Designing a label for Convertible Hood Cleaner (also 6 more labels to design in the future)

We have a range of cleaning products which we need to update label designs

This competition is just for one design but once a winner has been selected we have a lot more work for you including 6 more labels and a new logo.

Please see files for content. This product is very popular but the label is outdated.

Size of label - 110mm x 75mm
This will be a sticky label to be added to a sachet (white ziplock pouch)

Colors

Designer to choose colors to be used in the design.

```html
<!DOCTYPE html>
<html lang="en">
<head>
<meta charset="utf-8">
<title>Heavy Duty Convertible Soft Top Cleaner – Label</title>
<link href="https://fonts.googleapis.com/css2?family=Aldrich&family=Roboto+Condensed:wght@700&display=swap" rel="stylesheet">
<style>
  :root {
    --edge-maroon: #4a1616;
    --deep-red: #8e1a1a;
    --burst-red: #e0231f;
    --glow-orange: #ff6a4a;
    --core-white: #ffffff;
    --text-white: #ffffff;
  }
  html, body {
    margin: 0;
    padding: 0;
    width: 819px;
    height: 1200px;
    overflow: hidden;
    background: var(--edge-maroon);
  }
  .label {
    position: relative;
    width: 819px;
    height: 1200px;
    overflow: hidden;
  }
  .label__burst {
    position: absolute;
    inset: 0;
    background:
      radial-gradient(circle at 50% 56%,
        var(--core-white) 0,
        #ffe6dc 60px,
        var(--glow-orange) 170px,
        var(--burst-red) 330px,
        var(--deep-red) 560px,
        var(--edge-maroon) 820px);
  }
  .label__title {
    position: absolute;
    top: 160px;
    left: 0;
    right: 0;
    margin: 0;
    text-align: center;
    font-family: "Aldrich", sans-serif;
    font-weight: 400;
    font-size: 60px;
    line-height: 80px;
    letter-spacing: 2px;
    color: var(--text-white);
  }
  .label__title span { display: block; }
  .label__brand {
    position: absolute;
    top: 612px;
    left: 0;
    right: 0;
    text-align: center;
    font-family: "Aldrich", sans-serif;
    font-size: 86px;
    line-height: 100px;
    letter-spacing: 2px;
    color: var(--text-white);
  }
  .label__claims {
    position: absolute;
    left: 0;
    right: 0;
    text-align: center;
    font-family: "Roboto Condensed", sans-serif;
    font-weight: 700;
    font-size: 42px;
    line-height: 55px;
    color: var(--text-white);
    margin: 0;
  }
  .label__claims span { display: block; }
  .label__claims--usage { top: 880px; }
  .label__claims--targets { top: 1041px; }
</style>
</head>
<body>
  <div class="label">
    <div class="label__burst" role="img" aria-label="Red light-ray burst glowing white at the centre"></div>

    <h1 class="label__title">
      <span>HEAVY DUTY</span>
      <span>CONVERTIBLE</span>
      <span>SOFT TOP CLEANER</span>
    </h1>

    <div class="label__brand">PIT LANE PRO</div>

    <p class="label__claims label__claims--usage">
      <span>QUICK AND EASY TO USE</span>
      <span>FOR PROFESSIONAL RESULTS</span>
    </p>

    <p class="label__claims label__claims--targets">
      <span>CLEANS: DIRT- GRIME-STAINS</span>
      <span>MOULD AND MILDEW</span>
    </p>
  </div>
</body>
</html>
```